Website for Plumbing Company, Mr. BoilBright

I need a 7-page fully HTML-coded website for my plumbing company, Mr. BoilBright. We specialize in installation, repair, and replacement of both gas and electric water heaters. Although we offer both tankless (on-demand) water heaters and standard (with tank) water heaters, most of our business is related to standard (with tank) water heaters in the USA market.

These are the pages I need:
1. Home page with sections such as About Us, Our Services, Why Choose Us, Testimonials, Location Map (Palm Beach County Florida), Quote Request Form, Join Our Newsletter, Mission Statement, etc.

2. Gas Water Heaters

3. Electric Water Heaters

4. Tankless Water Heaters

5. About Us

6. Contact Us

7. Privacy Policy, Terms & Conditions

Be sure to mention the following points:
1. Same-Day Service
2. Best Price Guarantee
3. 100% Satisfaction Rating
4. 15-Year Warranty on Water Heater & Parts
5. Lifetime Warranty on Workmanship
*All Warranties are Transferrable Upon Home Sale

Once design is selected and finalized, I need the website coded in a standard HTML/CSS and temporarily hosted on your development server so I can see the website functionality that is not observable from screenshots, such as section animations, etc. Once those details are finalized, I will move the source code to my server and complete the project.

Target Market(s)

Residential Home Owners and Business Owners

Industry/Entity Type

Plumbing, Home Services, Remodeling, Construction

Coding

Coded - Design and coding required

Number of Pages Required

5+ page

Colors
0054AA
0677BA
7BADD7
CADEEF
E8F1F8
FFC000
F8CF3A
FAE287
FDF2CF
FEFAEE
EE7325
F08F49
F5BC92
FAE3D3
FDF4ED

Requirements
Must have
• Clean, colorful, and professional

```html
<!DOCTYPE html>
<html lang="en">
<head>
<meta charset="utf-8">
<title>Terms &amp; Conditions – Mr. BoilBright</title>
<link href="https://fonts.googleapis.com/css2?family=Poppins:wght@400;500;600;700;800&display=swap" rel="stylesheet">
<style>
:root{
  --blue-dark:#0054AA;
  --blue:#0677BA;
  --blue-mid:#7BADD7;
  --blue-light:#CADEEF;
  --blue-pale:#E8F1F8;
  --orange:#EE7325;
  --orange-soft:#F08F49;
  --yellow:#FFC000;
  --navy:#0B1733;
  --ink:#1d2230;
  --text:#5b606b;
  --white:#ffffff;
}
*{margin:0;padding:0;box-sizing:border-box}
html,body{width:1200px;height:2668px;overflow:hidden}
body{font-family:"Poppins",sans-serif;background:var(--white);color:var(--text);position:relative}

.site-header{position:absolute;top:0;left:0;width:1200px;height:152px;background:var(--white);z-index:3}
.topbar{position:absolute;top:0;right:0;width:720px;height:42px;background:var(--blue-dark);border-bottom-left-radius:24px;display:flex;align-items:center;justify-content:flex-end;gap:34px;padding-right:60px;color:var(--white);font-size:14px}
.topbar span{display:flex;align-items:center;gap:8px}
.brand{position:absolute;left:48px;top:18px;display:flex;align-items:center;gap:12px;height:110px;padding:0 22px;background:var(--blue-pale);border-radius:14px}
.brand-dot{width:40px;height:40px;border-radius:50%;background:var(--orange)}
.brand-name{font-size:26px;font-weight:700;color:var(--blue-dark)}
.main-nav{position:absolute;right:80px;top:60px;display:flex;align-items:center;gap:36px;font-size:14px;font-weight:600;color:var(--ink);text-transform:uppercase}
.btn-quote{background:var(--orange);color:var(--white);padding:14px 26px;border-radius:30px;display:flex;align-items:center;gap:10px}

.hero{position:absolute;top:152px;left:0;width:1200px;height:760px;overflow:hidden}
.hero-photo{position:absolute;inset:0;background:linear-gradient(100deg,#0a3f86 0%,#1a64b3 40%,#6f9fcc 70%,#c6d8ea 100%)}
.hero-title{position:absolute;left:60px;top:300px;color:var(--white);font-size:64px;font-weight:800;line-height:1.05;text-transform:uppercase}
.breadcrumb{position:absolute;left:62px;top:460px;color:var(--white);font-size:14px;font-weight:500}
.breadcrumb b{color:var(--yellow);font-weight:600}
.hero-wave{position:absolute;left:0;bottom:0;width:1200px;height:190px}
.scroll-icon{position:absolute;left:586px;top:805px;z-index:4}

.terms{position:absolute;top:940px;left:0;width:1200px;height:1260px;overflow:hidden;padding:0 60px}
.terms h1{text-align:center;font-size:40px;font-weight:800;color:var(--ink);text-transform:uppercase}
.title-bar{width:90px;height:4px;background:var(--orange);margin:10px auto 26px;border-radius:2px}
.terms h2{font-size:16px;font-weight:700;color:var(--ink);margin:20px 0 6px}
.terms p{font-size:13.5px;line-height:1.75;margin-bottom:8px}
.tick-list{list-style:none;margin:4px 0 8px}
.tick-list li{font-size:13.5px;line-height:1.7;padding-left:30px;position:relative;margin-bottom:6px}
.tick-list li::before{content:"";position:absolute;left:0;top:3px;width:18px;height:18px;border-radius:50%;background:var(--orange)}
.tick-list li::after{content:"";position:absolute;left:6px;top:7px;width:5px;height:8px;border:solid var(--white);border-width:0 2px 2px 0;transform:rotate(45deg)}

.site-footer{position:absolute;top:2212px;left:0;width:1200px;height:456px;background:linear-gradient(180deg,#0d1b3c 0%,#0a1530 100%);color:#c9d2e3}
.footer-inner{position:absolute;top:66px;left:60px;right:60px;display:flex}
.footer-brand{width:370px}
.footer-brand .brand{position:static;width:max-content;height:92px}
.follow{margin-top:40px;color:var(--white);font-weight:700;font-size:17px}
.socials{display:flex;gap:14px;margin-top:16px}
.socials span{width:38px;height:38px;border-radius:50%;background:var(--orange)}
.footer-col{width:260px}
.footer-col h3{color:var(--white);font-size:17px;font-weight:700;margin-bottom:16px}
.footer-col li{list-style:none;font-size:13.5px;margin-bottom:12px}
.contact-col{width:270px}
.contact-col li{display:flex;gap:12px;align-items:flex-start}
.contact-icon{flex:none;width:30px;height:30px;border-radius:50%;background:var(--orange);display:flex;align-items:center;justify-content:center}
.copyright{position:absolute;bottom:0;left:0;width:100%;height:52px;border-top:1px solid rgba(255,255,255,.12);display:flex;align-items:center;justify-content:center;font-size:13px}
</style>
</head>
<body>

<header class="site-header">
  <div class="topbar">
    <span><svg width="14" height="14" viewBox="0 0 24 24" fill="#fff"><path d="M6.6 10.8a15 15 0 0 0 6.6 6.6l2.2-2.2a1 1 0 0 1 1-.25 11.4 11.4 0 0 0 3.6.57 1 1 0 0 1 1 1V20a1 1 0 0 1-1 1A17 17 0 0 1 3 4a1 1 0 0 1 1-1h3.5a1 1 0 0 1 1 1c0 1.25.2 2.45.57 3.57a1 1 0 0 1-.25 1z"/></svg>(Phone) (555) 210-0148</span>
    <span><svg width="15" height="12" viewBox="0 0 24 18" fill="#fff"><path d="M2 0h20a2 2 0 0 1 2 2v14a2 2 0 0 1-2 2H2a2 2 0 0 1-2-2V2a2 2 0 0 1 2-2zm0 3v.4l10 6.2 10-6.2V3L12 9 2 3z"/></svg>(Email) info@mrboilbright.com</span>
  </div>
  <div class="brand"><span class="brand-dot"></span><span class="brand-name">Mr. BoilBright</span></div>
  <nav class="main-nav">
    <span>Home</span><span>Services</span><span>About</span><span>Testimonials</span><span>Contact</span>
    <span class="btn-quote">Get Quote <svg width="14" height="12" viewBox="0 0 14 12"><path d="M0 6h12M7 1l5 5-5 5" stroke="#fff" stroke-width="2" fill="none"/></svg></span>
  </nav>
</header>

<section class="hero">
  <div class="hero-photo" role="img" aria-label="Technician servicing a water heater in a bright utility room, tinted blue"></div>
  <h1 class="hero-title">Terms &amp;<br>Conditions</h1>
  <div class="breadcrumb">Home &nbsp;&gt;&nbsp; <b>Tankless Water Heaters</b></div>
  <svg class="hero-wave" viewBox="0 0 1200 190" preserveAspectRatio="none">
    <path d="M0 120 Q600 -10 1200 120 L1200 190 L0 190Z" fill="#fff"/>
    <path d="M0 100 Q600 -30 1200 100" stroke="#0054AA" stroke-width="6" fill="none"/>
  </svg>
</section>
<svg class="scroll-icon" width="28" height="42" viewBox="0 0 28 42"><rect x="2" y="2" width="24" height="38" rx="12" fill="#fff" stroke="#0054AA" stroke-width="3"/><rect x="12" y="10" width="4" height="9" rx="2" fill="#EE7325"/></svg>

<main class="terms">
  <h1>Terms &amp; Conditions</h1>
  <div class="title-bar"></div>
  <p>Lorem Ipsum is simply dummy text of the printing and typesetting industry. Lorem Ipsum has been the industry's standard dummy text ever since the 1500s, when an unknown printer took a galley of type and scrambled it to make a type specimen book. It has survived not only five centuries, but also the leap into electronic typesetting, remaining essentially unchanged. It was popularised in the 1960s with the release of Letraset sheets containing Lorem Ipsum passages.</p>

  <h2>similique sunt in culpa qui officia deserunt mollitia animi, id est laborum et dolorum fuga</h2>
  <p>Because those who do not know how to pursue pleasure rationally encounter consequences that are extremely painful. Nor again is there anyone who loves or pursues or desires to obtain pain of itself.</p>
  <ul class="tick-list">
    <li>adipisci velit, sed quia non numquam eius modi tempora incidunt ut labore et dolore magnam aliquam quaerat voluptatem. Ut enim ad minima veniam, quis nostrum ullam corporis suscipit laboriosam, nisi ut aliquid ex ea commodi consequatur.</li>
    <li>the master-builder of human happiness. No one rejects, dislikes, or avoids pleasure itself, because it is pleasure, but because those who do not know.</li>
    <li>omnis voluptas assumenda est, omnis dolor repellendus. Temporibus autem quibusdam et aut officiis debitis aut rerum necessitatibus saepe eveniet ut et voluptates repudiandae.</li>
  </ul>

  <h2>At vero eos et accusamus et iusto odio dignissimos ducimus qui blanditiis</h2>
  <p>On the other hand, we denounce with righteous indignation and dislike men who are so beguiled and demoralized by the charms of pleasure of the moment, so blinded by desire, that they cannot foresee the pain and trouble that are bound to ensue; and equal blame belongs to those who fail in their duty through weakness of will, which is the same as saying through shrinking from toil and pain. These cases are perfectly simple and easy to distinguish. In a free hour.</p>
  <p>the great explorer of the truth, the master-builder of human happiness. No one rejects, dislikes, or avoids pleasure itself, because it is pleasure but because those who do not know.</p>

  <h2>Ut enim ad minim veniam, quis nostrud exercitation ullamco laboris</h2>
  <p>Sed ut perspiciatis unde omnis iste natus error sit voluptatem accusantium doloremque laudantium, totam rem aperiam, eaque ipsa quae ab illo inventore veritatis et quasi architecto beatae vitae dicta sunt explicabo. Nemo enim ipsam voluptatem quia voluptas sit aspernatur aut odit aut fugit, sed quia consequuntur magni dolores eos qui ratione voluptatem sequi.</p>
  <p>the great explorer of the truth, the master-builder of human happiness. No one rejects, dislikes, or avoids pleasure itself, because it is pleasure but because those who do not know.</p>

  <h2>The standard Lorem Ipsum passage</h2>
  <p>But I must explain to you how all this mistaken idea of denouncing pleasure and praising pain was born and I will give you a complete account of the system, and expound the actual teachings of the great explorer of the truth, the master-builder of human happiness. No one rejects, dislikes, but I must explain to you how all this mistaken idea of denouncing pleasure and praising pain was born and I will give you a complete account of the system, and expound the actual teachings of the great explorer of the truth, the master-builder of human happiness. No one rejects, dislikes, or avoids pleasure itself, because it is pleasure, but because those who do not know how to pursue pleasure rationally encounter consequences that are extremely painful. Nor again is there anyone.</p>

  <h2>Section de Finibus Bonorum et Malorum</h2>
  <p>Lorem ipsum dolor sit amet, consectetur adipiscing elit, sed do eiusmod tempor incididunt ut labore et dolore magna aliqua. Ut enim ad minim veniam, quis nostrud exercitation ullamco laboris nisi ut aliquip ex ea commodo consequat. Duis aute irure dolor in reprehenderit in voluptate velit esse cillum dolore eu fugiat nulla pariatur. Excepteur sint occaecat cupidatat non proident, sunt in culpa qui officia deserunt mollit anim id est laborum.</p>
  <ul class="tick-list">
    <li>adipisci velit, sed quia non numquam eius modi tempora incidunt ut labore et dolore magnam aliquam quaerat voluptatem. Ut enim ad minima veniam, quis nostrum ullam corporis suscipit laboriosam, nisi ut aliquid ex ea commodi consequatur.</li>
    <li>omnis voluptas assumenda est, omnis dolor repellendus. Temporibus autem quibusdam et aut officiis debitis aut rerum necessitatibus saepe eveniet ut et voluptates repudiandae.</li>
  </ul>
</main>

<footer class="site-footer">
  <div class="footer-inner">
    <div class="footer-brand">
      <div class="brand"><span class="brand-dot"></span><span class="brand-name">Mr. BoilBright</span></div>
      <div class="follow">Follow Us Now</div>
      <div class="socials"><span></span><span></span><span></span></div>
    </div>
    <div class="footer-col">
      <h3>Company</h3>
      <ul><li>Home</li><li>About Us</li><li>Gas Water Heater</li><li>Electric Water Heater</li><li>Tankless Water Heater</li><li>Careers</li><li>Contact Us</li></ul>
    </div>
    <div class="footer-col">
      <h3>Legal Links</h3>
      <ul><li>Sitemap</li><li>Privacy Policy</li><li>Terms of Use</li></ul>
    </div>
    <div class="footer-col contact-col">
      <h3>Contact Us</h3>
      <ul>
        <li><span class="contact-icon"><svg width="13" height="13" viewBox="0 0 24 24" fill="#fff"><path d="M6.6 10.8a15 15 0 0 0 6.6 6.6l2.2-2.2a1 1 0 0 1 1-.25 11.4 11.4 0 0 0 3.6.57 1 1 0 0 1 1 1V20a1 1 0 0 1-1 1A17 17 0 0 1 3 4a1 1 0 0 1 1-1h3.5a1 1 0 0 1 1 1c0 1.25.2 2.45.57 3.57a1 1 0 0 1-.25 1z"/></svg></span>(555) 210-0148</li>
        <li><span class="contact-icon"><svg width="14" height="11" viewBox="0 0 24 18" fill="#fff"><path d="M2 0h20a2 2 0 0 1 2 2v14a2 2 0 0 1-2 2H2a2 2 0 0 1-2-2V2a2 2 0 0 1 2-2zm0 3v.4l10 6.2 10-6.2V3L12 9 2 3z"/></svg></span>info@mrboilbright.com</li>
        <li><span class="contact-icon"><svg width="11" height="14" viewBox="0 0 20 26" fill="#fff"><path d="M10 0a10 10 0 0 1 10 10c0 7-10 16-10 16S0 17 0 10A10 10 0 0 1 10 0zm0 6a4 4 0 1 0 0 8 4 4 0 0 0 0-8z"/></svg></span>410 Harbor Lane, Brightwater, USA</li>
      </ul>
    </div>
  </div>
  <div class="copyright">© 2024 Mr. BoilBright. All rights reserved.</div>
</footer>

</body>
</html>
```